" Minha principal atuação é como consultor de empresas atuando na aceleração das mesmas. Utilizo em minhas consultorias técnicas de coach e metodologias de aceleração de empresas. Meu foco é fazer com que a empresa/empreendedor se desenvolva e cresça rapidamente gerando resultados cada dia maiores para o empreendimento. Também dou mentoria para empreendedores e palestras e treinamentos diversos na área de empreendedorismo. "

```html
<!DOCTYPE html>
<html lang="pt-BR">
<head>
<meta charset="UTF-8">
<title>Rafael Tavares — Cartão de Visita</title>
<link rel="stylesheet" href="https://fonts.googleapis.com/css2?family=Montserrat:wght@400;600&display=swap">
<style>
  :root {
    --page: #e6e4e1;
    --card: #ffffff;
    --charcoal: #4a4a4a;
    --charcoal-dark: #3d3d3d;
    --amber: #f5b800;
    --text: #4d4d4d;
    --muted: #8a8a8a;
  }
  html, body {
    margin: 0;
    width: 1200px;
    height: 1200px;
    overflow: hidden;
    background: var(--page);
    font-family: "Montserrat", sans-serif;
  }
  .sheet {
    width: 1200px;
    height: 1200px;
    display: flex;
    flex-direction: column;
    align-items: center;
    justify-content: center;
    gap: 56px;
  }
  .card {
    position: relative;
    width: 900px;
    height: 514px;
    background: var(--card);
    box-shadow: 0 6px 24px rgba(0,0,0,0.12);
    overflow: hidden;
  }
  .card-shapes {
    position: absolute;
    inset: 0;
  }
  .front-identity {
    position: absolute;
    left: 150px;
    top: 210px;
    display: flex;
    align-items: center;
    gap: 22px;
  }
  .identity-square {
    width: 52px;
    height: 52px;
    background: var(--amber);
  }
  .identity-name {
    margin: 0;
    font-size: 50px;
    font-weight: 600;
    letter-spacing: 1px;
    color: var(--charcoal);
    line-height: 1;
  }
  .identity-tagline {
    margin: 10px 0 0;
    font-size: 15.5px;
    font-weight: 600;
    letter-spacing: 1.2px;
    color: var(--amber);
    text-transform: uppercase;
  }
  .back-identity {
    position: absolute;
    left: 70px;
    top: 90px;
    display: flex;
    align-items: center;
    gap: 16px;
  }
  .back-identity .identity-square {
    width: 36px;
    height: 36px;
  }
  .back-identity .identity-name {
    font-size: 34px;
    color: #ffffff;
  }
  .contact-list {
    position: absolute;
    right: 80px;
    top: 250px;
    margin: 0;
    padding: 0;
    list-style: none;
    display: flex;
    flex-direction: column;
    gap: 26px;
  }
  .contact-item {
    display: flex;
    align-items: center;
    gap: 22px;
    font-size: 20px;
    letter-spacing: 1.5px;
    color: var(--text);
  }
  .contact-icon {
    width: 40px;
    height: 40px;
    flex: none;
  }
</style>
</head>
<body>
<main class="sheet">

  <section class="card card-front">
    <svg class="card-shapes" viewBox="0 0 900 514" aria-hidden="true">
      <polygon points="640,0 900,0 900,70 880,70 880,12 652,12" fill="var(--amber)"/>
      <polygon points="0,444 20,444 20,502 248,502 260,514 0,514" fill="var(--amber)"/>
      <polygon points="620,514 900,514 900,430 700,430" fill="var(--charcoal)"/>
    </svg>
    <div class="front-identity">
      <div class="identity-square"></div>
      <div>
        <h1 class="identity-name">RAFAEL TAVARES</h1>
        <p class="identity-tagline">Consultoria e Aceleração de Empresas</p>
      </div>
    </div>
  </section>

  <section class="card card-back">
    <svg class="card-shapes" viewBox="0 0 900 514" aria-hidden="true">
      <polygon points="0,0 600,0 290,514 0,514" fill="var(--charcoal)"/>
      <polygon points="600,0 900,0 900,14 612,14 604,22" fill="var(--amber)"/>
      <polygon points="880,0 900,0 900,90 880,90" fill="var(--amber)"/>
      <polygon points="0,500 300,500 290,514 0,514" fill="var(--amber)"/>
      <polygon points="0,424 20,424 20,514 0,514" fill="var(--amber)"/>
    </svg>
    <div class="back-identity">
      <div class="identity-square"></div>
      <h2 class="identity-name">RAFAEL TAVARES</h2>
    </div>
    <ul class="contact-list">
      <li class="contact-item">
        <svg class="contact-icon" viewBox="0 0 40 40" aria-hidden="true">
          <circle cx="20" cy="20" r="20" fill="var(--charcoal)"/>
          <rect x="14" y="9" width="12" height="22" rx="2" fill="none" stroke="#fff" stroke-width="2"/>
          <circle cx="20" cy="27" r="1.3" fill="#fff"/>
        </svg>
        <span>(00) 0000-0000</span>
      </li>
      <li class="contact-item">
        <svg class="contact-icon" viewBox="0 0 40 40" aria-hidden="true">
          <circle cx="20" cy="20" r="20" fill="var(--charcoal)"/>
          <rect x="10" y="13" width="20" height="14" rx="1.5" fill="none" stroke="#fff" stroke-width="2"/>
          <polyline points="10,14 20,21 30,14" fill="none" stroke="#fff" stroke-width="2"/>
        </svg>
        <span>contato@empresa.com.br</span>
      </li>
      <li class="contact-item">
        <svg class="contact-icon" viewBox="0 0 40 40" aria-hidden="true">
          <circle cx="20" cy="20" r="20" fill="var(--charcoal)"/>
          <circle cx="20" cy="20" r="10" fill="none" stroke="#fff" stroke-width="2"/>
          <ellipse cx="20" cy="20" rx="4.5" ry="10" fill="none" stroke="#fff" stroke-width="1.6"/>
          <line x1="10" y1="20" x2="30" y2="20" stroke="#fff" stroke-width="1.6"/>
        </svg>
        <span>www.seusite.com.br</span>
      </li>
    </ul>
  </section>

</main>
</body>
</html>
```